cup design rebranding with modern design

8 oz and 4 oz cup redesign

i will share my existing cups

also i want different slogans for coffee on the back also my logo is attached any color also a design for take away holder

be creative

modern

and elegant

i need it to be innovative

Industry/Entity Type

Coffee Shop

Contact Information for Business Card

up to the designer

Font styles to use
Decorative
Script

Colors

Designer to choose colors to be used in the design.

Requirements
Must have
• logo
• instagram account @tidewellcoffee
• slogan english or arabic

```html
<!DOCTYPE html>
<html lang="en">
<head>
<meta charset="UTF-8">
<title>Tidewell Coffee — Business Card</title>
<link href="https://fonts.googleapis.com/css2?family=Noto+Sans:wght@400;700&display=swap" rel="stylesheet">
<style>
  :root {
    --page: #ffffff;
    --card-light: #e1e1e1;
    --card-dark: #39383a;
    --ink: #231f20;
    --ink-soft: #3a3a3a;
    --paper: #f2f2f2;
  }
  html, body {
    margin: 0;
    width: 1200px;
    height: 1200px;
    overflow: hidden;
    background: var(--page);
    font-family: "Noto Sans", sans-serif;
  }
  .canvas { position: relative; width: 1200px; height: 1200px; }
  .card {
    position: absolute;
    left: 174px;
    width: 851px;
    height: 472px;
    border-radius: 40px;
  }
  .card--front { top: 88px; background: var(--card-light); color: var(--ink); }
  .card--back { top: 640px; background: var(--card-dark); color: var(--paper); }

  .brand {
    position: absolute;
    text-align: center;
    font-family: "Noto Sans", sans-serif;
  }
  .brand__name {
    font-weight: 400;
    letter-spacing: 0.14em;
    line-height: 1;
  }
  .brand__tag {
    font-weight: 400;
    letter-spacing: 0.06em;
    line-height: 1;
  }
  .card--front .brand { left: 62px; top: 200px; width: 212px; color: var(--ink-soft); }
  .card--front .brand__name { font-size: 38px; }
  .card--front .brand__tag { font-size: 12.5px; margin-top: 14px; }
  .card--back .brand { left: 346px; top: 206px; width: 159px; }
  .card--back .brand__name { font-size: 29px; }
  .card--back .brand__tag { font-size: 9.6px; margin-top: 10px; }

  .details { position: absolute; left: 354px; top: 128px; }
  .details__title { margin: 0; font-size: 26px; font-weight: 700; line-height: 1; }
  .details__subtitle { margin: 3px 0 0; font-size: 16px; line-height: 1.1; }
  .rule { width: 52px; height: 2px; background: var(--ink); margin: 15px 0 12px; }
  .contacts { list-style: none; margin: 0; padding: 0; font-size: 16px; line-height: 21px; }
  .contacts li { display: flex; align-items: flex-start; margin-bottom: 1px; }
  .contacts svg { width: 14px; height: 14px; margin: 3px 10px 0 0; flex: none; }
  .contacts .pin svg { height: 17px; margin-top: 2px; }
  .slogan { margin: 0; font-size: 13px; font-weight: 700; }
</style>
</head>
<body>
<main class="canvas">
  <section class="card card--front">
    <div class="brand">
      <div class="brand__name">TIDEWELL</div>
      <div class="brand__tag">SPECIALTY COFFEE HOUSE</div>
    </div>
    <div class="details">
      <h1 class="details__title">TIDEWELL COFFEE</h1>
      <p class="details__subtitle">Specialty Coffee House</p>
      <div class="rule"></div>
      <ul class="contacts">
        <li class="pin">
          <svg viewBox="0 0 14 17" aria-hidden="true"><path d="M7 0.5a6 6 0 0 1 6 6c0 4.2-6 10-6 10s-6-5.8-6-10a6 6 0 0 1 6-6z" fill="var(--ink)"/><circle cx="7" cy="6.5" r="2.2" fill="var(--card-light)"/></svg>
          <span>Harbor Lane Plaza<br>opposite the Old Lighthouse Gardens-Marbel</span>
        </li>
        <li>
          <svg viewBox="0 0 14 14" aria-hidden="true"><path d="M3 1.2l2.2 2.6-1.2 1.6c.8 1.8 2.3 3.3 4.1 4.1l1.6-1.2 2.6 2.2-1.3 2c-5 0-9.5-4.5-9.5-9.5z" fill="none" stroke="var(--ink)" stroke-width="1.2" stroke-linejoin="round"/></svg>
          <span>+9715 2081 6634</span>
        </li>
        <li>
          <svg viewBox="0 0 14 14" aria-hidden="true"><circle cx="7" cy="7" r="6" fill="none" stroke="var(--ink)" stroke-width="1.4"/></svg>
          <span>@tidewellcoffee</span>
        </li>
        <li>
          <svg viewBox="0 0 14 14" aria-hidden="true"><rect x="0.7" y="2.5" width="12.6" height="9" fill="none" stroke="var(--ink)" stroke-width="1.1"/><path d="M0.7 2.5l6.3 5 6.3-5M0.7 11.5l4.6-4.2M13.3 11.5l-4.6-4.2" fill="none" stroke="var(--ink)" stroke-width="1.1"/></svg>
          <span>info@tidewellch.com</span>
        </li>
      </ul>
      <div class="rule"></div>
      <p class="slogan">Coffee can make your life longer.</p>
    </div>
  </section>

  <section class="card card--back">
    <div class="brand">
      <div class="brand__name">TIDEWELL</div>
      <div class="brand__tag">SPECIALTY COFFEE HOUSE</div>
    </div>
  </section>
</main>
</body>
</html>
```